Tourism marketing and PR agency needs a new header design for their website landing page and social

We currently have a landing page (www.vortek-partners.de/en) design that symbolizes the worldwide locations of our international tourism clients but it looks too much like an airline route map. Thus the search for a new header that should be more modern, bolder and better reflect the nature of our tourism business - that being leisure and business travel. We are a marketing and PR agency, we are not a travel agency. We would also like to use the core design as a header for our Twitter and Facebook profiles and would need adapted layouts. Our slogan COMMUNICATION, MARKETING & SALES IN ONE can also be integrated. We would like to see designs, which contrast the colors of our logo.

We would prefer graphics over photographs.

Target Market(s)

Potential clients from tourism and hotel industry, tour operators, industry partners, travel agencies, journalists and digital influencers

Industry/Entity Type

Tourism

Coding

Coded - Design and coding required

Number of Pages Required

1 page

Font styles to use
Sans Serif

Requirements
Must have
• Emotion and a link to marketing, PR and travel (but no plane)
Should not have
• We don't want anything with a globe design or a map

```html
<!DOCTYPE html>
<html lang="en">
<head>
<meta charset="utf-8">
<title>Vortek Partners – Communication Marketing &amp; Sales in One</title>
<link href="https://fonts.googleapis.com/css2?family=Raleway:wght@400;500;600&family=Open+Sans:wght@400;600&display=swap" rel="stylesheet">
<style>
:root{
  --sky:#82c2e7;
  --sky-deep:#5eb0e0;
  --sky-pale:#d6ebf7;
  --night:#000;
  --navy:#1b2a5c;
  --white:#fff;
  --button:#3a3a3a;
  --ghost:#3b3b3b;
}
*{margin:0;padding:0;box-sizing:border-box}
html,body{width:777px;height:1200px;overflow:hidden;background:var(--night)}
body{position:relative;font-family:"Open Sans",Arial,sans-serif;color:var(--white)}
.abs{position:absolute}

/* hero */
.hero{left:0;top:0;width:777px;height:616px;
  background:radial-gradient(ellipse 260px 330px at 395px 390px,#4a4038 0%,#2f2b28 40%,transparent 75%),
             radial-gradient(ellipse at 50% 40%,#2c2c2c 0%,#1e1e1e 55%,#111 100%)}
.hero-icons{left:0;top:0;width:777px;height:616px}
.hero-band{left:0;top:365px;width:777px;height:251px;background:rgba(0,0,0,.38)}
.topbar{left:0;top:0;width:777px;height:53px;border-bottom:1px solid #555}
.brand{left:30px;top:0;width:100px;height:88px;background:var(--white);
  display:flex;flex-direction:column;align-items:center;justify-content:center;gap:5px}
.brand-name{font-family:"Raleway",sans-serif;font-weight:600;font-size:17px;color:var(--navy)}
.brand-mark{width:10px;height:10px;background:var(--navy)}
.nav{right:30px;top:0;height:53px;display:flex;list-style:none}
.nav li{height:53px;display:flex;align-items:center;padding:0 17px;font-size:9px;font-weight:600;letter-spacing:.2px}
.nav li.active{background:var(--sky)}
.headline{left:0;top:202px;width:777px;text-align:center;font-family:"Raleway",sans-serif;
  font-weight:500;font-size:45px;line-height:53px;letter-spacing:.3px}

/* services */
.connector{left:108px;top:448px;width:551px;height:1px;background:var(--white)}
.service{width:172px;text-align:center}
.service-icon{width:88px;height:88px;margin:0 auto;border-radius:50%;border:2px solid var(--white);padding:3px;background:#1a1a1a}
.service-icon .disc{width:100%;height:100%;border-radius:50%;background:var(--sky);display:flex;align-items:center;justify-content:center}
.service-icon.light .disc{background:var(--white)}
.service h3{font-family:"Raleway",sans-serif;font-weight:600;font-size:11px;color:var(--sky);margin-top:10px;letter-spacing:.3px}
.service p{width:162px;margin:7px auto 0;font-size:7.4px;line-height:10.5px}
.service a{display:inline-block;font-size:7.4px;color:var(--sky);margin-top:4px;text-decoration:none}

/* newsletter */
.newsletter{left:0;top:616px;width:777px;height:144px;background:var(--sky)}
.newsletter h2{position:absolute;top:24px;width:100%;text-align:center;font-family:"Raleway",sans-serif;font-weight:500;font-size:24px}
.field{top:77px;width:251px;height:33px;background:var(--sky-pale);font-size:7.5px;color:#666;padding:12px 10px}
.signup{left:570px;top:77px;width:180px;height:33px;background:var(--button);font-size:11px;display:flex;align-items:center;justify-content:center;letter-spacing:.5px}

/* welcome */
.welcome-title{left:0;top:784px;width:777px;text-align:center;font-family:"Raleway",sans-serif;font-weight:500;font-size:24px;color:var(--sky-deep)}
.welcome-text{left:122px;top:823px;width:533px;text-align:center;font-size:7.6px;line-height:13.5px}
.card{top:889px;width:221px}
.card-photo{height:128px}
.card-label{margin-top:13px;height:19px;background:var(--sky);font-size:9px;padding:3px 8px}
.card-title{position:absolute;top:60px;left:0;width:100%;text-align:center;font-family:"Raleway",sans-serif;font-weight:600;font-size:11px;color:var(--sky)}
.dot{top:1076px;width:6px;height:6px;border-radius:50%;background:var(--white)}
.dot.current{background:var(--sky)}

/* footer */
.footer{left:0;top:1118px;width:777px;height:82px;background:var(--sky)}
.footer-links{top:30px;width:100%;text-align:center;font-size:7.5px}
.copyright{top:50px;width:100%;text-align:center;font-size:6px}
.social{right:40px;top:36px;display:flex;gap:15px}
.social span{width:9px;height:9px;border-radius:50%;background:rgba(255,255,255,.55)}
</style>
</head>
<body>

<section class="abs hero" role="img" aria-label="Dark photo of a hand pointing upward toward floating media icons"></section>

<svg class="abs hero-icons" viewBox="0 0 777 616" aria-hidden="true" fill="var(--ghost)">
  <!-- calendar -->
  <g transform="translate(358,26)">
    <rect x="0" y="8" width="66" height="60" rx="5"/>
    <g fill="#262626"><rect x="7" y="28" width="10" height="7"/><rect x="21" y="28" width="10" height="7"/><rect x="35" y="28" width="10" height="7"/><rect x="49" y="28" width="10" height="7"/><rect x="7" y="40" width="10" height="7"/><rect x="21" y="40" width="10" height="7"/><rect x="35" y="40" width="10" height="7"/><rect x="49" y="40" width="10" height="7"/><rect x="7" y="52" width="10" height="7"/><rect x="21" y="52" width="10" height="7"/><rect x="35" y="52" width="10" height="7"/></g>
  </g>
  <!-- speech bubble -->
  <path d="M212 122h50a6 6 0 0 1 6 6v35a6 6 0 0 1-6 6h-14l-4 12-10-12h-22a6 6 0 0 1-6-6v-35a6 6 0 0 1 6-6z"/>
  <!-- envelope -->
  <g transform="translate(512,132)">
    <rect width="66" height="48" rx="3"/>
    <path d="M3 4l30 22 30-22M3 44l22-18M63 44l-22-18" fill="none" stroke="#242424" stroke-width="4"/>
  </g>
  <!-- house -->
  <path d="M180 262v-28l-6 4-4-6 40-28 40 28-4 6-6-4v28h-18v-18h-24v18z" opacity=".75"/>
  <!-- eye -->
  <path d="M556 262q32-36 70 0q-38 36-70 0z" opacity=".55"/>
  <!-- camera -->
  <g transform="translate(205,320)">
    <rect x="0" y="10" width="64" height="44" rx="5"/>
    <rect x="20" y="2" width="24" height="10" rx="2"/>
    <circle cx="32" cy="32" r="14" fill="#262626"/><circle cx="32" cy="32" r="8"/>
  </g>
  <!-- film reel -->
  <g transform="translate(542,346)">
    <circle r="33"/>
    <g fill="#262626"><circle cy="-17" r="8"/><circle cx="-17" r="8"/><circle cx="17" r="8"/><circle cy="17" r="8"/></g>
    <path d="M20 24l14 12" stroke="var(--ghost)" stroke-width="6"/>
  </g>
  <!-- speaker -->
  <g transform="translate(350,395)" opacity=".8">
    <path d="M0 14h10l18-14v50l-18-14h-10z"/>
    <path d="M36 12q10 13 0 26M44 4q18 21 0 42" fill="none" stroke="var(--ghost)" stroke-width="5"/>
  </g>
</svg>

<div class="abs hero-band"></div>

<header class="abs topbar">
  <ul class="abs nav">
    <li class="active">HOME</li><li>CLIENTS</li><li>TEAM</li><li>SERVICES</li><li>CONTACT</li><li>NEWSROOM</li>
  </ul>
</header>
<div class="abs brand"><span class="brand-name">Vortek</span><span class="brand-mark"></span></div>

<h1 class="abs headline">COMMUNICATION MARKETING<br>&amp; SALES IN ONE</h1>

<div class="abs connector"></div>

<div class="abs service" style="left:22px;top:404px">
  <div class="service-icon light"><div class="disc">
    <svg width="36" height="30" viewBox="0 0 36 30" fill="#82c2e7"><rect x="11" y="2" width="12" height="10"/><rect x="3" y="14" width="12" height="10"/><rect x="17" y="14" width="12" height="10"/></svg>
  </div></div>
  <h3>PUBLIC RELATIONS</h3>
  <p>Lorem ipsum dolor sit amet, consectetur edit adipiscing elit, sed do eiusmod tempor incididunt utdolore magna aliqua.</p>
  <a href="#">Read More ▸</a>
</div>

<div class="abs service" style="left:204px;top:404px">
  <div class="service-icon"><div class="disc">
    <svg width="32" height="32" viewBox="0 0 32 32" fill="none" stroke="#fff" stroke-width="4"><path d="M4 30V4h12v18M12 10v20h16V2"/></svg>
  </div></div>
  <h3>MARKETING &amp; SALES</h3>
  <p>Lorem ipsum dolor sit amet, consectetur edit adipiscing elit, sed do eiusmod tempor incididunt utdolore magna aliqua.</p>
  <a href="#">Read More ▸</a>
</div>

<div class="abs service" style="left:394px;top:404px">
  <div class="service-icon"><div class="disc">
    <svg width="28" height="36" viewBox="0 0 28 36"><rect x="2" y="1" width="24" height="34" fill="#fff"/><g fill="#82c2e7"><rect x="6" y="5" width="4" height="4"/><rect x="12" y="5" width="4" height="4"/><rect x="18" y="5" width="4" height="4"/><rect x="6" y="12" width="4" height="4"/><rect x="12" y="12" width="4" height="4"/><rect x="18" y="12" width="4" height="4"/><rect x="6" y="19" width="4" height="4"/><rect x="12" y="19" width="4" height="4"/><rect x="18" y="19" width="4" height="4"/><rect x="11" y="27" width="6" height="8"/></g></svg>
  </div></div>
  <h3>MICE SERVICES</h3>
  <p>Lorem ipsum dolor sit amet, consectetur edit adipiscing elit, sed do eiusmod tempor incididunt utdolore a aliqua.</p>
  <a href="#">Read More ▸</a>
</div>

<div class="abs service" style="left:573px;top:404px">
  <div class="service-icon"><div class="disc">
    <svg width="32" height="32" viewBox="0 0 32 32" fill="#fff"><circle cx="8" cy="16" r="5"/><circle cx="24" cy="7" r="5"/><circle cx="24" cy="25" r="5"/><path d="M8 16L24 7M8 16l16 9" stroke="#fff" stroke-width="2.5"/></svg>
  </div></div>
  <h3>SOCIAL MEDIA</h3>
  <p>Lorem ipsum dolor sit amet, consectetur edit adipiscing elit, sed do eiusmod tempor incididunt magna aliqua.</p>
  <a href="#">Read More ▸</a>
</div>

<section class="abs newsletter">
  <h2>Join our Newsletter!</h2>
  <div class="abs field" style="left:36px">Enter Your Name</div>
  <div class="abs field" style="left:304px">Enter Your Email id</div>
  <div class="abs signup">SIGN UP</div>
</section>

<h2 class="abs welcome-title">Welcome to Vortek Partners</h2>
<p class="abs welcome-text">It is burning. Now it is: get out of the building. To safety. Escape and rescue plans are an important guide and also an essential tool for training people for the right behavior in case of fire. With the professional preparation of escape and rescue plans we contribute our part in ensuring that people with you in case of a fire in the shortest find ways out of the building.</p>

<div class="abs card" style="left:32px">
  <div class="card-photo" role="img" aria-label="Hotel resort building lit at night" style="background:linear-gradient(180deg,#1a1d24,#3b2f22 70%,#2a2218);position:relative"><span class="card-title">SEEWALD GOLF RESORT</span></div>
  <div class="card-label">Public Relations</div>
</div>
<div class="abs card" style="left:278px">
  <div class="card-photo" role="img" aria-label="Group of people in blue shirts jumping on a beach" style="background:linear-gradient(180deg,#3f7fd0,#8ab8ea 60%,#d9d6cc)"></div>
  <div class="card-label">Public Relations</div>
</div>
<div class="abs card" style="left:526px">
  <div class="card-photo" role="img" aria-label="Alpine hotel with green garden and mountains" style="background:linear-gradient(180deg,#8fb3d8,#4d7a3a 45%,#3fa12e)"></div>
  <div class="card-label">Public Relations</div>
</div>

<span class="abs dot" style="left:372px"></span>
<span class="abs dot current" style="left:385px"></span>
<span class="abs dot" style="left:398px"></span>

<footer class="abs footer">
  <div class="abs footer-links">Home &nbsp;/&nbsp; Clients &nbsp;/&nbsp; Team &nbsp;/&nbsp; Services &nbsp;/&nbsp; Contact &nbsp;/&nbsp; Newsroom</div>
  <div class="abs copyright">© All Rights Reserved. Copyrights @Company Name .2016</div>
  <div class="abs social"><span></span><span></span><span></span><span></span><span></span></div>
</footer>

</body>
</html>
```